PPT Template for an investment fund to use in their pitchbooks

Our firm is an international investment fund and are seeking a PPT template to use in our pitch book (and subsequent PPTs). We would need a template for a title slide and then subsequent text/info slides. A clean & uncluttered feel is preferred as well as no watermark on slides. Please see our logo attached. The logo color code is #19478d. Font is Gotham-Medium.

Target Market(s)

Sophisticated investors

Industry/Entity Type

Finance

Colors
ffffff
0356a4

```html
<!DOCTYPE html>
<html lang="en">
<head>
<meta charset="utf-8">
<title>Halvard Capital Partners – Presentation Template</title>
<link href="https://fonts.googleapis.com/css2?family=Montserrat:wght@400;500;600;700&display=swap" rel="stylesheet">
<style>
:root{
  --brand:#19478d;
  --brand-deep:#163f7f;
  --brand-tint:#2d5ca8;
  --ink:#1c2a44;
  --grey-bg:#e7e7e8;
  --tile-grey:#e3e4e6;
  --dark-box:#3c3d40;
  --white:#ffffff;
}
*{box-sizing:border-box;margin:0;padding:0}
html,body{width:1200px;height:2664px;overflow:hidden}
body{background:var(--grey-bg);font-family:"Montserrat",Arial,sans-serif;color:var(--ink);position:relative}
.slide{position:absolute;width:545px;height:409px;background:var(--white);overflow:hidden}
.col-l{left:44px}.col-r{left:612px}
.row1{top:44px}.row2{top:478px}.row3{top:911px}.row4{top:1344px}.row5{top:1777px}.row6{top:2210px}
.abs{position:absolute}
.brand-name{position:absolute;font-weight:600;font-size:7px;letter-spacing:.3px;color:var(--brand);display:flex;align-items:center;gap:4px;text-transform:uppercase;white-space:nowrap}
.brand-name::before{content:"";width:7px;height:7px;background:currentColor;display:block}
.brand-name.on-dark{color:var(--white)}
.brand-name.top-right{right:26px;top:20px}
.url{position:absolute;left:30px;bottom:12px;font-size:5.5px;color:var(--brand);font-weight:500}
.page-no{position:absolute;right:18px;bottom:12px;font-size:5px;color:var(--brand)}
.title-lg{font-weight:500;font-size:21px;line-height:1.2;text-transform:uppercase}
.title-sm{font-weight:600;font-size:10.5px;color:var(--brand);text-transform:uppercase;letter-spacing:.2px}
.title-sm::after{content:"";display:block;width:22px;height:2px;background:var(--brand);margin-top:6px}
.rule{display:block;width:42px;height:2px;background:currentColor;margin:12px 0}
.copy{font-size:5.6px;line-height:1.4}
.copy p+p{margin-top:6px}
.justify{text-align:justify}
.white{color:var(--white)}
.blue{color:var(--brand)}
.photo{position:absolute}
.sub{font-weight:500;font-size:14px;color:var(--brand)}
.sub-sm{font-weight:600;font-size:8px;color:var(--brand);margin-bottom:3px}
.feature-list .item{margin-bottom:17px}
.num-item{position:absolute;width:170px}
.num-item h4{font-weight:500;font-size:11px;color:var(--brand)}
.num-item p{font-size:8px;line-height:1.3}
.num-box{position:absolute;width:47px;height:55px;color:var(--white);font-size:17px;display:flex;align-items:center;justify-content:center}
.quad{position:absolute;width:154px;height:107px;display:flex;align-items:center;justify-content:center}
.quad p{font-size:7px;font-weight:600;line-height:1.35;color:var(--white);padding:0 18px}
</style>
</head>
<body>

<!-- Cover, blue -->
<section class="slide col-l row1">
  <div class="photo" role="img" aria-label="City skyline photograph tinted brand blue" style="left:0;top:126px;width:545px;height:283px;background:linear-gradient(180deg,#3563ad 0%,#24519c 60%,#1e4a93 100%)"></div>
  <div class="abs" style="left:0;top:0;width:545px;height:126px;background:var(--white)"></div>
  <div class="brand-name top-right" style="top:80px;right:72px">Halvard Capital Partners</div>
  <div class="abs white" style="left:68px;top:199px;width:260px">
    <h1 class="title-lg">Presentation title<br>goes here</h1>
    <span class="rule"></span>
    <div class="copy" style="font-weight:500">Lorem ipsum dolor sit amet, consectetur adipiscing elit, sed do eiusmod tempor incididunt ut labore et dolore magna aliqua. Ut enim ad minim veniam, quis nostrud exercitation ullamco laboris nisi ut aliquip ex ea commodo consequat. Duis aute irure dolor in reprehenderit in voluptate velit esse cillum dolore eu fugiat nulla pariatur excepteur sint.</div>
  </div>
  <div class="abs white" style="left:68px;top:358px;font-size:8px;font-weight:600">www.halvardcp.com</div>
</section>

<!-- Cover, white -->
<section class="slide col-r row1">
  <div class="brand-name" style="left:36px;top:94px">Halvard Capital Partners</div>
  <div class="abs blue" style="left:34px;top:152px;width:250px">
    <h1 class="title-lg">Presentation title<br>goes here</h1>
    <div class="copy" style="margin-top:12px">Lorem ipsum dolor sit amet, consectetur adipiscing elit, sed do eiusmod tempor incididunt ut labore et dolore magna aliqua. Ut enim ad minim veniam, quis nostrud exercitation ullamco laboris nisi ut aliquip ex ea commodo consequat. Duis aute irure dolor in reprehenderit in voluptate velit esse cillum dolore eu fugiat nulla pariatur excepteur sint.</div>
  </div>
  <div class="abs blue" style="left:34px;top:310px;font-size:8px;font-weight:600">www.halvardcp.com</div>
  <div class="photo" role="img" aria-label="City at dusk with river and lit skyline" style="left:270px;top:82px;width:275px;height:327px;background:linear-gradient(160deg,#9fc0e4 0%,#5d7fae 45%,#3a4a6a 75%,#7a5a3c 100%)"></div>
</section>

<!-- Who we are -->
<section class="slide col-l row2">
  <div class="abs" style="left:48px;top:135px"><h2 class="title-sm">Who we are</h2></div>
  <div class="photo" role="img" aria-label="Portrait of a senior executive in a grey suit" style="left:0;top:205px;width:181px;height:204px;background:linear-gradient(180deg,#e9ecef 0%,#c9ced5 55%,#6e747d 100%)"></div>
  <div class="photo" role="img" aria-label="Downtown skyline under a blue sky" style="left:181px;top:0;width:364px;height:192px;background:linear-gradient(180deg,#2f78d0 0%,#7fb0e8 60%,#8d98a8 80%,#4b5566 100%)"></div>
  <div class="abs" style="left:181px;top:192px;width:364px;height:217px;background:var(--brand)"></div>
  <div class="brand-name on-dark top-right">Halvard Capital Partners</div>
  <div class="abs copy white justify" style="left:210px;top:225px;width:310px">
    <p>Lorem ipsum dolor sit amet, consectetur adipiscing elit, sed do eiusmod tempor incididunt ut labore et dolore magna aliqua. Ut enim ad minim veniam, quis nostrud exercitation ullamco laboris nisi ut aliquip ex ea commodo consequat.</p>
    <p>Duis aute irure dolor in reprehenderit in voluptate velit esse cillum dolore eu fugiat nulla pariatur.</p>
    <p>Excepteur sint occaecat cupidatat non proident, sunt in culpa qui officia deserunt mollit anim id est laborum. Sed ut perspiciatis unde omnis iste natus error sit voluptatem accusantium doloremque laudantium, totam rem aperiam, eaque ipsa quae ab illo inventore veritatis.</p>
    <p>Et quasi architecto beatae vitae dicta sunt explicabo. Nemo enim ipsam voluptatem quia voluptas sit aspernatur aut odit aut fugit, sed quia consequuntur magni dolores eos qui ratione.</p>
  </div>
  <div class="abs white" style="left:30px;bottom:12px;font-size:5.5px">www.halvardcp.com</div>
  <div class="page-no white">1</div>
</section>

<!-- Subheading with triangle image -->
<section class="slide col-r row2">
  <div class="brand-name top-right">Halvard Capital Partners</div>
  <svg class="abs" style="left:40px;top:46px" width="230" height="156" viewBox="0 0 230 156">
    <polygon points="112,8 216,150 100,150" fill="var(--brand)"/>
    <polygon points="110,0 204,142 0,142" fill="#d9dde2" role="img" aria-label="Laptop showing charts on a desk"/>
  </svg>
  <div class="abs" style="left:223px;top:226px;width:298px">
    <h3 class="sub">Subheading text goes here</h3>
    <div class="copy justify" style="margin-top:6px">
      <p>Lorem ipsum dolor sit amet, consectetur adipiscing elit, sed do eiusmod tempor incididunt ut labore et dolore magna aliqua. Ut enim ad minim veniam, quis nostrud exercitation ullamco laboris nisi ut aliquip ex ea commodo consequat.</p>
      <p>Lorem ipsum dolor sit amet, consectetur adipiscing elit, sed do eiusmod tempor incididunt ut labore et dolore magna aliqua. Ut enim ad minim veniam, quis nostrud exercitation ullamco laboris nisi ut aliquip ex ea commodo consequat. Duis aute irure dolor in reprehenderit in voluptate velit esse cillum dolore eu fugiat nulla pariatur. Excepteur sint occaecat cupidatat non proident.</p>
      <p>Sunt in culpa qui officia deserunt mollit anim id est laborum. Sed ut perspiciatis unde omnis iste natus error sit voluptatem accusantium doloremque laudantium, totam rem aperiam, eaque ipsa quae ab illo invent.</p>
    </div>
  </div>
  <div class="url">www.halvardcp.com</div><div class="page-no">1</div>
</section>

<!-- Three icons -->
<section class="slide col-l row3">
  <div class="brand-name top-right">Halvard Capital Partners</div>
  <div class="abs" style="left:53px;top:65px"><h2 class="title-sm">Title goes here</h2></div>
  <div class="abs copy" style="left:53px;top:110px;width:445px">Lorem ipsum dolor sit amet, consectetur adipiscing elit, sed do eiusmod tempor incididunt ut labore et dolore magna aliqua. Ut enim ad minim veniam, quis nostrud exercitation ullamco laboris nisi ut aliquip ex ea commodo consequat. Duis aute irure dolor in reprehenderit in voluptate velit esse cillum dolore eu fugiat nulla pariatur. Excepteur sint occaecat cupidatat non proident, sunt in culpa qui officia deserunt mollit anim id est laborum. Sed ut perspiciatis unde omnis iste natus error sit voluptatem accusantium d.</div>
  <svg class="abs" style="left:52px;top:168px" width="440" height="86" viewBox="0 0 440 86" fill="none" stroke="var(--brand)" stroke-width="2">
    <polygon points="56,2 112,84 1,84"/>
    <polygon points="215,2 271,84 160,84"/>
    <polygon points="382,2 438,84 327,84"/>
    <rect x="42" y="52" width="26" height="13" rx="1.5" stroke-width="2"/><rect x="68" y="55" width="3" height="7" fill="var(--brand)" stroke="none"/>
    <polygon points="56,54 52,60 56,60 54,64 60,57 56,57 58,54" fill="var(--brand)" stroke="none"/>
    <circle cx="215" cy="58" r="11"/><path d="M204 58h22M215 47c-6 6-6 16 0 22M215 47c6 6 6 16 0 22"/><circle cx="215" cy="58" r="16" stroke-width="1.5" stroke-dasharray="8 6"/>
    <path d="M376 66v-4c-4-2-6-6-6-10a12 12 0 0 1 24 0c0 4-2 8-6 10v4z"/><path d="M377 70h10M378 73h8"/>
  </svg>
  <div class="abs copy justify" style="left:52px;top:283px;width:114px"><p>Lorem ipsum dolor sit amet, consectetur adipiscing elit, sed do eiusmod tempor incididunt ut labore et dolore magna aliqua. Ut enim ad minim veniam.</p><p>Lorem ipsum dolor sit amet, consectetur adipiscing elit, sed do eiusmod tempor incididunt ut labore et</p></div>
  <div class="abs copy justify" style="left:215px;top:283px;width:114px"><p>Lorem ipsum dolor sit amet, consectetur adipiscing elit, sed do eiusmod tempor incididunt ut labore et dolore magna aliqua. Ut enim ad minim veniam.</p><p>Lorem ipsum dolor sit amet, consectetur adipiscing elit, sed do eiusmod tempor incididunt ut labore et</p></div>
  <div class="abs copy justify" style="left:378px;top:283px;width:114px"><p>Lorem ipsum dolor sit amet, consectetur adipiscing elit, sed do eiusmod tempor incididunt ut labore et dolore magna aliqua. Ut enim ad minim veniam.</p><p>Lorem ipsum dolor sit amet, consectetur adipiscing elit, sed do eiusmod tempor incididunt ut labore et</p></div>
  <div class="url">www.halvardcp.com</div><div class="page-no">1</div>
</section>

<!-- Framed photo + list -->
<section class="slide col-r row3">
  <div class="brand-name top-right">Halvard Capital Partners</div>
  <div class="abs" style="left:61px;top:32px"><h2 class="title-sm">Title goes here</h2></div>
  <div class="abs" style="left:46px;top:102px;width:178px;height:266px;background:var(--brand)"></div>
  <div class="photo" role="img" aria-label="Black and white photo of a business handshake over a desk" style="left:62px;top:90px;width:166px;height:268px;background:linear-gradient(135deg,#2a2a2a 0%,#8a8a8a 45%,#d8d8d8 70%,#4a4a4a 100%)"></div>
  <div class="abs feature-list" style="left:251px;top:95px;width:200px">
    <div class="item"><h4 class="sub-sm">Subheading goes here</h4><div class="copy">Lorem ipsum dolor sit amet, consectetur adipiscing elit, sed do eiusmod tempor incididunt ut labore et dolore magna aliqua. Ut enim ad minim veniam, quis nostrud exercitation ullamco laboris nisi ut aliquip ex ea commodo consequat.</div></div>
    <div class="item"><h4 class="sub-sm">Subheading goes here</h4><div class="copy">Lorem ipsum dolor sit amet, consectetur adipiscing elit, sed do eiusmod tempor incididunt ut labore et dolore magna aliqua. Ut enim ad minim veniam, quis nostrud exercitation ullamco laboris nisi ut aliquip ex ea commodo consequat.</div></div>
    <div class="item"><h4 class="sub-sm">Subheading goes here</h4><div class="copy">Lorem ipsum dolor sit amet, consectetur adipiscing elit, sed do eiusmod tempor incididunt ut labore et dolore magna aliqua. Ut enim ad minim veniam, quis nostrud exercitation ullamco laboris nisi ut aliquip ex ea commodo consequat.</div></div>
    <div class="item"><h4 class="sub-sm">Subheading goes here</h4><div class="copy">Lorem ipsum dolor sit amet, consectetur adipiscing elit, sed do eiusmod tempor incididunt ut labore et dolore magna aliqua. Ut enim ad minim veniam, quis nostrud exercitation ullamco laboris nisi ut aliquip ex ea commodo consequat.</div></div>
  </div>
  <div class="url">www.halvardcp.com</div><div class="page-no">1</div>
</section>

<!-- Section divider -->
<section class="slide col-l row4">
  <div class="photo" role="img" aria-label="Water droplet rippling on a blue water surface" style="left:0;top:0;width:545px;height:409px;background:radial-gradient(ellipse at 45% 55%,#3a6ab2 0%,#22569f 45%,#17417f 100%)"></div>
  <div class="brand-name on-dark top-right">Halvard Capital Partners</div>
  <div class="abs white" style="left:197px;top:180px;width:260px">
    <h2 class="title-lg" style="font-size:19px">Section title text<br>goes here</h2>
    <div class="copy" style="margin-top:10px;font-weight:500">Lorem ipsum dolor sit amet, consectetur adipiscing elit, sed do eiusmod tempor incididunt ut labore et</div>
  </div>
</section>

<!-- Banner + text -->
<section class="slide col-r row4">
  <div class="brand-name top-right">Halvard Capital Partners</div>
  <div class="photo" role="img" aria-label="Glass office buildings against a pale blue sky" style="left:0;top:65px;width:545px;height:115px;background:linear-gradient(90deg,#8ecbef 0%,#4f9ad8 45%,#2a5f9e 100%)"></div>
  <div class="abs white" style="left:82px;top:117px"><h2 class="title-sm" style="color:var(--white)">Title goes here</h2></div>
  <style>.slide .banner-title::after{background:var(--white)}</style>
  <div class="abs copy white" style="left:235px;top:101px;width:310px;height:67px;background:var(--brand);padding:8px 12px;font-weight:500">Lorem ipsum dolor sit amet, consectetur adipiscing elit, sed do eiusmod tempor incididunt ut labore et dolore magna aliqua. Ut enim ad minim veniam, quis nostrud exercitation ullamco laboris nisi ut aliquip ex ea commodo consequat. Duis aute irure dolor in reprehenderit in voluptate velit esse cillum dolore eu fugiat nulla pariatur. Excepteur sint occaecat cupidatat non proident, sunt in culpa qui officia deserunt mollit anim id est laborum. Sed</div>
  <div class="abs" style="left:101px;top:243px;width:360px">
    <h3 class="sub" style="font-size:11.5px">Subheading text goes here</h3>
    <div class="copy" style="margin-top:8px">
      <p>Lorem ipsum dolor sit amet, consectetur adipiscing elit, sed do eiusmod tempor incididunt ut labore et dolore magna aliqua. Ut enim ad minim veniam, quis nostrud exercitation ullamco laboris nisi ut aliquip ex ea commodo consequat.</p>
      <p style="margin-top:9px">Lorem ipsum dolor sit amet, consectetur adipiscing elit, sed do eiusmod tempor incididunt ut labore et dolore magna aliqua. Ut enim ad minim veniam, quis nostrud exercitation ullamco laboris nisi ut aliquip ex ea commodo consequat.</p>
    </div>
  </div>
  <div class="url">www.halvardcp.com</div><div class="page-no">1</div>
</section>

<!-- Tall photo + statement -->
<section class="slide col-l row5">
  <div class="photo" role="img" aria-label="City skyline and lit bridge at dusk" style="left:0;top:0;width:235px;height:409px;background:linear-gradient(180deg,#7fa6d6 0%,#5b7fb1 35%,#2f3c55 65%,#a0703e 100%)"></div>
  <div class="abs" style="left:235px;top:0;width:5px;height:409px;background:var(--brand)"></div>
  <div class="abs white" style="left:30px;bottom:12px;font-size:5.5px">www.halvardcp.com</div>
  <div class="brand-name" style="left:271px;top:98px">Halvard Capital Partners</div>
  <div class="abs" style="left:271px;top:132px;width:240px">
    <p style="font-size:12px;font-weight:500;line-height:1.25;color:var(--ink)">Lorem ipsum dolor sit amet, consectetur adipiscing elit, sed do eiusmod tempor incididunt ut labore et dolore magna aliqua.</p>
    <div class="copy" style="margin-top:8px">
      <p>Ut enim ad minim veniam, quis nostrud exercitation ullamco laboris nisi ut aliquip ex ea commodo consequat. Duis aute irure dolor in reprehenderit in voluptate velit esse cillum dolore eu fugiat nulla pariatur. Excepteur sint occaecat cupidatat non proident, sunt in culpa qui officia deserunt mollit anim id est laborum. Sed ut perspiciatis unde omnis iste natus error sit voluptatem accusantium doloremque laudantium, totam rem aperiam.</p>
      <p>Eaque ipsa quae ab illo inventore veritatis et quasi architecto beatae vitae dicta sunt explicabo. Nemo enim ipsam voluptatem quia voluptas sit aspernatur aut odit aut fugit, sed quia consequuntur magni dolores eos qui ratione voluptatem sequi nesciunt. Neque porro quisquam est, qui dolorem ipsum quia dolor sit amet, consectetur, adipisci velit, sed quia non numquam eius modi tempora incidunt ut labore et dolore magnam aliquam quaerat voluptatem.</p>
    </div>
  </div>
  <div class="page-no">1</div>
</section>

<!-- Numbered items -->
<section class="slide col-r row5">
  <div class="brand-name top-right">Halvard Capital Partners</div>
  <div class="abs" style="left:38px;top:46px"><h2 class="title-sm">Title goes here</h2></div>
  <div class="abs copy" style="left:38px;top:100px;width:460px">Lorem ipsum dolor sit amet, consectetur adipiscing elit, sed do eiusmod tempor incididunt ut labore et dolore magna aliqua. Ut enim ad minim veniam, quis nostrud exercitation ullamco laboris nisi ut aliquip ex ea commodo consequat. Duis aute irure dolor in reprehenderit in voluptate velit esse cillum dolore eu fugiat nulla pariatur. Excepteur sint occaecat cupidatat non proident, sunt in culpa qui officia deserunt mollit anim id est laborum. Sed ut pers.</div>
  <div class="num-item" style="left:30px;top:173px;text-align:right"><h4>Title here</h4><p>Lorem ipsum dolor sit amet<br>consectetur adipiscing elit sed.</p></div>
  <div class="num-box" style="left:210px;top:169px;background:var(--brand)">1</div>
  <div class="num-box" style="left:287px;top:169px;background:var(--dark-box)">2</div>
  <div class="num-item" style="left:349px;top:175px"><h4>Title here</h4><p>Lorem ipsum dolor sit amet<br>consectetur adipiscing elit sed.</p></div>
  <div class="num-item" style="left:30px;top:258px;text-align:right"><h4>Title here</h4><p>Lorem ipsum dolor sit amet<br>consectetur adipiscing elit sed.</p></div>
  <div class="num-box" style="left:210px;top:254px;background:var(--dark-box)">3</div>
  <div class="num-box" style="left:287px;top:254px;background:var(--brand)">4</div>
  <div class="num-item" style="left:349px;top:260px"><h4>Title here</h4><p>Lorem ipsum dolor sit amet<br>consectetur adipiscing elit sed.</p></div>
  <div class="url">www.halvardcp.com</div><div class="page-no">1</div>
</section>

<!-- Quadrant grid -->
<section class="slide col-l row6">
  <div class="brand-name top-right">Halvard Capital Partners</div>
  <div class="abs" style="left:103px;top:46px"><h2 class="title-sm">Title goes here</h2></div>
  <div class="quad" style="left:119px;top:91px;background:var(--tile-grey)">
    <svg width="40" height="44" viewBox="0 0 40 44" fill="none" stroke="var(--brand)" stroke-width="2.5"><path d="M20 3 36 9v12c0 10-7 17-16 20C11 38 4 31 4 21V9z"/><path d="M20 14v12" stroke-linecap="round"/><circle cx="20" cy="31" r="1.5" fill="var(--brand)"/></svg>
  </div>
  <div class="quad" style="left:273px;top:91px;background:var(--brand)"><p>Lorem ipsum dolor sit amet, consectetur adipiscing elit, sed do eiusmod tempor.</p></div>
  <div class="quad" style="left:119px;top:198px;background:var(--brand)"><p>Lorem ipsum dolor sit amet, consectetur adipiscing elit, sed do eiusmod tempor.</p></div>
  <div class="quad" style="left:273px;top:198px;background:var(--tile-grey)">
    <svg width="44" height="44" viewBox="0 0 44 44"><circle cx="22" cy="22" r="21" fill="var(--brand)"/><circle cx="22" cy="17" r="7" fill="var(--white)"/><path d="M9 35c3-7 8-9 13-9s10 2 13 9" fill="var(--white)"/></svg>
  </div>
  <div class="abs copy" style="left:119px;top:334px;width:300px;font-size:6.3px">Lorem ipsum dolor sit amet, consectetur adipiscing elit, sed do eiusmod tempor incididunt ut labore et dolore magna aliqua. Ut enim ad minim veniam, quis nostrud exercitation ullamco laboris nisi ut aliquip ex ea commodo consequat</div>
  <div class="url">www.halvardcp.com</div><div class="page-no">1</div>
</section>

<!-- Closing -->
<section class="slide col-r row6">
  <div class="photo" role="img" aria-label="Glass office tower against a light blue sky" style="left:0;top:0;width:545px;height:220px;background:linear-gradient(90deg,#1f5a93 0%,#4b8cc6 30%,#8cc4ea 60%,#b8def3 100%)"></div>
  <div class="abs" style="left:0;top:220px;width:545px;height:189px;background:var(--brand)"></div>
  <div class="brand-name on-dark" style="left:340px;top:128px;font-size:9px">Halvard Capital Partners</div>
  <p class="abs white" style="left:79px;top:290px;width:420px;font-size:10.5px;font-weight:500;line-height:1.35">Lorem ipsum dolor sit amet, consectetur adipiscing elit, sed do eiusmod tempor incididunt ut labore et dolore magna aliqua. Ut enim ad minim veniam, quis nostrud exercitation ullamco laboris nisi ut aliquip ex ea commodo consequat.</p>
</section>

</body>
</html>
```